Wordpress Design Project for Bin Hire company

Kestrel Skip Rentals is a Bin Hire company based in the Western Suburbs of Melbourne (Australia) and was established in 1995.
The colours of the Kestrel Skip Rentals logo are Pantone 188C (Burgundy) and 424C (Grey). We would like the site to include these colours throughout the site.

The current Kestrel Skip Rentals site (www.kestrelskiprentals-example.com.au) has been in operation for a number of years and as we have recently commenced a project to update the Logo and Corporate ID, a new Website is also appropriate.

The Kestrel Skip Rentals site only needs to be a simple site and is unlikely to consist of more than 20 pages. The site is primarily used for people to find our contact details, delivery areas and the measurements/size of of the bins we hire to our customers.

Industry/Entity Type

It Company

Requirements
Must have
• A contact page template (which sends an email) which can be used for a main contact page as well as long form response pages to enhance our 'call to action'
A separate enquiry/order form with configurable options will also be required.
A category (products) page will be required which will list all of our bins, a configurable excerpt of the page contents along with a single photo of each bin (a slider may be used also).
We also require the ability for potential customers to look each bin on it's own page as well as a large image, information about each bin and our terms and conditions.
We would also like configurable titles and meta code for each page.
The site will also need the ability to integrate with Tallyworth Metrics.

```html
<!DOCTYPE html>
<html lang="en">
<head>
<meta charset="utf-8">
<title>Kestrel Skip Rentals</title>
<link href="https://fonts.googleapis.com/css2?family=Arimo:wght@400;700&display=swap" rel="stylesheet">
<style>
:root{
  --blue:#1fa9dc;
  --blue-light:#5ccaf0;
  --teal-link:#1590b5;
  --orange:#e8562a;
  --orange-light:#f47a3c;
  --ink:#333;
  --muted:#555;
  --rule:#d6d6d6;
  --footer:#3b3b3b;
  --footer-deep:#2e2e2e;
  --footer-text:#d0d0d0;
  --white:#fff;
}
*{box-sizing:border-box;margin:0;padding:0}
html,body{width:1013px;height:1200px;overflow:hidden}
body{font-family:"Arimo",Arial,sans-serif;color:var(--ink);background:var(--white);position:relative}
.abs{position:absolute}
ul{list-style:none}

/* header */
.site-header{left:0;top:0;width:1013px;height:63px;background:var(--white);box-shadow:0 2px 3px rgba(0,0,0,.18);z-index:2}
.brand{left:74px;top:18px;display:flex;align-items:center;gap:10px}
.brand-mark{width:26px;height:26px;background:var(--blue);border-radius:50%}
.brand-name{font-size:19px;color:#555;letter-spacing:.3px}
.nav-item{position:absolute;top:15px;text-align:left;white-space:nowrap}
.nav-item small{display:block;font-size:10px;color:#999;margin-bottom:3px}
.nav-item span{font-size:13px;color:#222;text-transform:uppercase}
.nav-item.is-active span{display:inline-block;background:linear-gradient(#7fd5f3,#2aa7d8);color:#fff;padding:2px 5px 8px;border-radius:2px}
.nav-caret{display:block;width:8px;height:5px;margin:2px auto 0}

.connect-bar{left:74px;top:63px;width:865px;height:31px;border:1px solid var(--rule);border-top:none;border-radius:0 0 6px 6px;font-size:11px;color:#333;display:flex;align-items:center;justify-content:space-between;padding:0 9px 0 16px}
.social{display:flex;align-items:center;gap:5px}
.social i{display:inline-block;width:14px;height:14px;background:#3b6aa5;border-radius:2px}
.social i:last-child{background:#c33}

/* hero */
.hero{left:0;top:103px;width:1013px;height:270px;background:linear-gradient(#2db4e6,#6fd0f3)}
.hero-text{left:76px;top:38px;width:228px;color:var(--white);font-size:15px;line-height:20px}
.hero-text .big{font-size:26px;line-height:22px}
.btn{display:inline-flex;align-items:center;gap:8px;background:linear-gradient(var(--orange-light),var(--orange));color:#fff;text-transform:uppercase;border-radius:2px}
.hero-btn{left:74px;top:195px;width:145px;height:39px;font-size:16px;padding-left:15px}
.hero-photo{left:342px;top:15px;width:599px;height:236px;background:linear-gradient(135deg,#7a7468 0%,#c8c3ba 30%,#d12a22 55%,#9e1a15 80%,#5a5a52 100%);box-shadow:0 1px 4px rgba(0,0,0,.35)}
.slider-band{left:0;top:373px;width:1013px;height:16px;background:linear-gradient(#e4e4e4,#f6f6f6)}
.slider-dots{left:483px;top:375px;display:flex;gap:3px}
.slider-dots i{width:13px;height:13px;border-radius:50%;background:#777;box-shadow:inset 0 1px 2px #333}
.slider-dots i:first-child{background:#ccc;border:3px solid #777}

/* info columns */
.info-col h2{font-size:16px;font-weight:700;color:#333;margin-bottom:20px}
.info-col p{font-size:10px;line-height:15px;color:#333}
.info-col li{font-size:10px;color:#333;margin-bottom:9.5px;padding-left:14px;position:relative}
.info-col li::before{content:"";position:absolute;left:1px;top:2px;border-left:4px solid var(--orange);border-top:3.5px solid transparent;border-bottom:3.5px solid transparent}
.col-divider{width:1px;height:182px;background:var(--rule);top:418px}
.small-btn{height:21px;font-size:9px;padding:0 10px}

/* products */
.section-title{left:76px;top:612px;font-size:18px;font-weight:400;color:#333}
.section-rule{left:76px;top:638px;width:863px;height:1px;background:var(--rule)}
.product{width:200px}
.product-photo{width:200px;height:144px;background:linear-gradient(#6f8b4f 0%,#9aab84 35%,#b9bcc0 60%,#9c9a92 100%)}
.product h3{font-size:15px;font-weight:400;color:var(--teal-link);margin:14px 0 12px}
.product p{font-size:11px;line-height:13px;color:#444}

/* footer */
.site-footer{left:0;top:904px;width:1013px;height:247px;background:var(--footer);color:var(--footer-text)}
.footer-col h4{font-size:15px;font-weight:400;color:#fff;padding-bottom:8px;border-bottom:1px solid #666;margin-bottom:14px}
.footer-col p{font-size:11px;line-height:15px}
.links li{font-size:11px;line-height:13px;padding:0 0 6px 15px;border-bottom:1px solid #555;margin-bottom:7px}
.links li:last-child{border:none;margin-bottom:0}
.blog li{display:flex;gap:10px;margin-bottom:14px;font-size:10px;line-height:13px}
.blog .thumb{width:38px;height:30px;flex:none;background:linear-gradient(#7fa1b6,#c4c4bf)}
.blog b{font-weight:400;color:#fff}
.contact dl{display:grid;grid-template-columns:53px 1fr;font-size:11px;line-height:15px;margin-top:28px}
.footer-bottom{left:0;top:1151px;width:1013px;height:49px;background:var(--footer-deep);color:#ccc;font-size:10px}
.copyright{left:74px;top:19px}
.card-slot{top:10px;width:50px;height:30px;border-radius:2px}
</style>
</head>
<body>

<header class="site-header abs">
  <div class="brand abs"><span class="brand-mark"></span><span class="brand-name">Kestrel Skip Rentals</span></div>
  <nav class="main-nav">
    <div class="nav-item is-active" style="left:503px;"><small>Welcome</small><span>Home</span></div>
    <div class="nav-item" style="left:593px;"><small>What We Do</small><span>Product List</span>
      <svg class="nav-caret" viewBox="0 0 8 5"><path d="M0 0l4 5 4-5" fill="none" stroke="#2aa7d8" stroke-width="1.5"/></svg></div>
    <div class="nav-item" style="left:724px;"><small>We are good at</small><span>Delivery Area</span>
      <svg class="nav-caret" viewBox="0 0 8 5"><path d="M0 0l4 5 4-5" fill="none" stroke="#2aa7d8" stroke-width="1.5"/></svg></div>
    <div class="nav-item" style="left:861px;"><small>Stay in Touch</small><span>Contact Us</span>
      <svg class="nav-caret" viewBox="0 0 8 5"><path d="M0 0l4 5 4-5" fill="none" stroke="#2aa7d8" stroke-width="1.5"/></svg></div>
  </nav>
</header>

<div class="connect-bar abs">
  <div class="social">Connect:&nbsp; <i></i><i></i><i></i></div>
  <div>Call : + 03 9000 1234 / Mail : hello@kestrelskip-example.com.au</div>
</div>

<section class="hero abs">
  <p class="hero-text abs">Our bins range in size from 4 cubic metres through to 10 cubic metres. We also have <span class="big">20 cubic metre</span> bins. All bins have gates for easy access and most will fit in a standard driveway.</p>
  <a class="btn hero-btn abs">Read More
    <svg width="8" height="11" viewBox="0 0 8 11"><path d="M0 0l8 5.5L0 11z" fill="#fff"/></svg></a>
  <div class="hero-photo abs" role="img" aria-label="Red waste collection truck with a worker in a high-visibility vest emptying a red bin"></div>
</section>
<div class="slider-band abs"></div>
<div class="slider-dots abs"><i></i><i></i><i></i></div>

<section class="info-col abs" style="left:74px;top:420px;width:210px;">
  <h2>Council Permits</h2>
  <p>A Council permit is required for bins placed outside your property i.e. on the road, nature strip or in a laneway/ROW.We will apply to Council for a permit on your behalf. Please call us for current permit rates for your area.</p>
</section>
<a class="btn small-btn abs" style="left:217px;top:579px;">Read More <svg width="5" height="7" viewBox="0 0 5 7"><path d="M0 0l5 3.5L0 7z" fill="#fff"/></svg></a>
<div class="col-divider abs" style="left:313px;"></div>

<section class="info-col abs" style="left:342px;top:420px;width:260px;">
  <h2>What can you put in the bin?</h2>
  <ul>
    <li>Household goods</li><li>Furniture and furnishings</li><li>Garden clippings (surcharge applies)</li>
    <li>Builders waste</li><li>Rock, soil or concrete in 4mt &amp; 6 mt only</li><li>Tyres and mattresses</li>
  </ul>
</section>
<a class="btn small-btn abs" style="left:516px;top:579px;">Read More <svg width="5" height="7" viewBox="0 0 5 7"><path d="M0 0l5 3.5L0 7z" fill="#fff"/></svg></a>
<div class="col-divider abs" style="left:617px;"></div>

<section class="info-col abs" style="left:642px;top:420px;width:280px;">
  <h2>What can’t you put in the bin?</h2>
  <ul>
    <li>No asbestos</li><li>No hazardous or toxic waste</li><li>No flammable waste</li><li>No batteries</li><li>No liquid waste</li>
  </ul>
</section>
<a class="btn small-btn abs" style="left:858px;top:579px;">Read More <svg width="5" height="7" viewBox="0 0 5 7"><path d="M0 0l5 3.5L0 7z" fill="#fff"/></svg></a>

<h2 class="section-title abs">Our Products</h2>
<div class="section-rule abs"></div>

<article class="product abs" style="left:76px;top:658px;">
  <div class="product-photo" role="img" aria-label="Grey 4 cubic metre walk-in bin on a gravel yard"></div>
  <h3>4 cubic metre walk in bin</h3><p>Length—4.1 metres &nbsp;&nbsp;&nbsp; Width—1.6 metres &nbsp;&nbsp; Height—0.650 metres</p>
</article>
<article class="product abs" style="left:294px;top:658px;">
  <div class="product-photo" role="img" aria-label="Grey 6 cubic metre walk-in bin beside a shed"></div>
  <h3>6 cubic metre walk in bin</h3><p>Length—4.1 metres &nbsp;&nbsp;&nbsp; Width—1.6 metres &nbsp;&nbsp; Height—0.650 metres</p>
</article>
<article class="product abs" style="left:516px;top:658px;">
  <div class="product-photo" role="img" aria-label="Grey 8 cubic metre walk-in bin under trees"></div>
  <h3>8 cubic metre walk in bin</h3><p>Length—4.1 metres &nbsp;&nbsp;&nbsp; Width—1.6 metres &nbsp;&nbsp; Height—0.650 metres</p>
</article>
<article class="product abs" style="left:743px;top:658px;">
  <div class="product-photo" role="img" aria-label="Grey 10 cubic metre walk-in bin in a yard"></div>
  <h3>10 cubic metre walk in bin</h3><p>Length—4.1 metres &nbsp;&nbsp;&nbsp; Width—1.6 metres &nbsp;&nbsp; Height—0.650 metres</p>
</article>

<footer class="site-footer abs">
  <div class="footer-col abs" style="left:76px;top:22px;width:204px;">
    <h4>About Us</h4>
    <p>Kestrel Skip Rentals supplies walk in bins for domestic and commercial use.</p><br>
    <p>Our bins range in size from 4 cubic metres through to 10 cubic metres. We also have 20 cubic metre bins. All bins have gates for easy access and most will fit in a standard driveway.</p>
  </div>
  <div class="footer-col links abs" style="left:306px;top:22px;width:168px;">
    <h4>Useful Links</h4>
    <ul><li>Frequently Asked Questions</li><li>Service Updates</li><li>Terms of Use</li><li>Privacy Policy</li><li>Help Desk</li><li>Product List</li><li>Delivery Area</li></ul>
  </div>
  <div class="footer-col blog abs" style="left:510px;top:22px;width:180px;">
    <h4>Latest from the Blog</h4>
    <ul>
      <li><span class="thumb" role="img" aria-label="Bin thumbnail"></span><span>Maecenas metus lore nulla, facili, pretium / <b>28 June 2012</b></span></li>
      <li><span class="thumb" role="img" aria-label="Bin thumbnail"></span><span>Maecenas metus lore nulla, facili, pretium / <b>28 June 2012</b></span></li>
      <li><span class="thumb" role="img" aria-label="Bin thumbnail"></span><span>Maecenas metus lore nulla, facili, pretium / <b>28 June 2012</b></span></li>
      <li><span class="thumb" role="img" aria-label="Bin thumbnail"></span><span>Maecenas metus lore nulla, facili, pretium / <b>28 June 2012</b></span></li>
    </ul>
  </div>
  <div class="footer-col contact abs" style="left:721px;top:22px;width:218px;">
    <h4>Contact Us</h4>
    <p>12 Harrier Lane<br>Kestrelton Vic 3999</p>
    <dl><dt>Phone:</dt><dd>03 9000 1234</dd><dt>Fax:</dt><dd>03 9000 5678</dd><dt>Mobile:</dt><dd>0400 000 111</dd><dt>E-mail:</dt><dd>hello@kestrelskip-example.com.au</dd></dl>
  </div>
</footer>
<div class="footer-bottom abs">
  <span class="copyright abs">© Copyrights 2012. All Rights Reserved.</span>
  <span class="card-slot abs" style="left:837px;background:#d8d8d8;"></span>
  <span class="card-slot abs" style="left:890px;background:#f2f2f2;"></span>
</div>

</body>
</html>
```